Photography Studio Prep Guide Design Needed

I have a prep guide I send to all parents who book a session - It is outdated and ugly. I want a gorgeous, clean, modern upscale look for the brochure I send.

I already have the text and can provide photos for the final design. I want the cover to be clean and upscale and modern, with a happy feel.

Target Market(s)

My clients for an upscale Newborn Photography Studio

Requirements
Must have
• space for my photos, an upscale clean feel
Nice to have
• I love color, but don't want the brochure to look busy. I love cream, white, pale pink.

```html
<!DOCTYPE html>
<html lang="en">
<head>
<meta charset="utf-8">
<title>Newborn Session Prep Guide</title>
<link rel="stylesheet" href="https://fonts.googleapis.com/css2?family=Libre+Caslon+Text&family=Playfair+Display:ital@1&family=Raleway:wght@300&display=swap">
<style>
  :root {
    --backdrop: #676767;
    --paper: #ffffff;
    --paper-soft: #e4e4e0;
    --green: #3aa56a;
    --green-muted: #5f9c7c;
    --pink: #e58bbd;
    --ink: #1d1d1d;
    --grey-text: #555555;
    --photo-cream: #e8dccf;
    --photo-blush: #d9b8a7;
  }
  * { box-sizing: border-box; margin: 0; padding: 0; }
  html, body { width: 1200px; height: 1200px; overflow: hidden; }
  body { background: var(--backdrop); position: relative; }

  .page { position: absolute; top: 281px; width: 514px; height: 641px; overflow: hidden; }
  .cover { left: 62px; background: var(--paper); }
  .inside { left: 633px; background: var(--paper-soft); }

  /* Cover */
  .cover-photo {
    position: absolute; left: 0; right: 0; top: 219px; bottom: 0;
    background: radial-gradient(ellipse at 55% 55%, var(--photo-blush) 0%, var(--photo-cream) 55%, #ddd4c8 100%);
  }
  .frame-top {
    position: absolute; left: 27px; width: 458px; top: 21px; height: 198px;
    border: 2px solid var(--green); border-bottom: none;
  }
  .frame-bottom {
    position: absolute; left: 27px; width: 458px; top: 219px; height: 394px;
    border: 2px solid var(--paper); border-top: none;
  }
  .brand { position: absolute; top: 42px; left: 0; right: 0; text-align: center; }
  .brand-dot { width: 22px; height: 22px; border-radius: 50%; background: var(--pink); margin: 0 auto 10px; opacity: .8; }
  .brand-name {
    font-family: "Libre Caslon Text", serif; font-size: 14px; color: var(--grey-text);
    letter-spacing: .5px;
  }
  .cover-title { position: absolute; top: 134px; left: 0; right: 0; text-align: center; }
  .cover-title .main {
    font-family: "Libre Caslon Text", serif; font-size: 33px; color: var(--green);
    line-height: 1; letter-spacing: .5px;
  }
  .cover-title .sub {
    font-family: "Playfair Display", serif; font-style: italic; font-size: 30px;
    color: #444; line-height: 1.1; margin-top: 2px;
  }

  /* Inside page */
  .intro-box {
    position: absolute; left: 45px; top: 26px; width: 436px; height: 144px;
    border: 1px solid var(--green-muted); text-align: center;
  }
  .intro-box h1 {
    font-family: "Playfair Display", serif; font-style: italic; font-weight: 400;
    font-size: 32px; line-height: 33px; margin-top: 12px; letter-spacing: 1px;
  }
  .intro-box h1 .first { color: var(--pink); display: block; }
  .intro-box h1 .second { color: var(--green-muted); display: block; }
  .intro-box p {
    font-family: "Raleway", sans-serif; font-weight: 300; font-size: 11px;
    color: var(--green-muted); line-height: 13px; margin-top: 14px;
  }
  .section { position: absolute; left: 41px; width: 440px; }
  .section h2 {
    font-family: "Playfair Display", serif; font-style: italic; font-weight: 400;
    font-size: 12px; color: var(--green-muted); margin-bottom: 4px;
  }
  .section p {
    font-family: Arial, Helvetica, sans-serif; font-size: 8.6px; line-height: 10.6px; color: var(--ink);
  }
  .section p.note { color: var(--green-muted); }
  .nursing { top: 191px; }
  .feeding { top: 292px; }
  .inside-photo {
    position: absolute; left: 0; right: 0; top: 414px; bottom: 0;
    background: linear-gradient(180deg, var(--paper-soft) 0%, #f1ede8 25%, #efe4da 60%, #f3efea 100%);
  }
</style>
</head>
<body>
  <section class="page cover">
    <div class="cover-photo" role="img" aria-label="Photo of a sleeping newborn wearing a flower headband and soft feather wings on a cream lace blanket"></div>
    <div class="frame-top"></div>
    <div class="frame-bottom"></div>
    <div class="brand">
      <div class="brand-dot"></div>
      <div class="brand-name">CLARA WHITFIELD PHOTOGRAPHY</div>
    </div>
    <div class="cover-title">
      <div class="main">NEWBORN SESSION</div>
      <div class="sub">Prep Guide</div>
    </div>
  </section>

  <section class="page inside">
    <div class="intro-box">
      <h1><span class="first">Parent Instructions &amp;</span><span class="second">Preparations</span></h1>
      <p>Congratulations on expecting a baby!<br>
      Here are my instructions to ensure a successful newborn photography session.<br>
      Please follow these instructions as closely as possible.</p>
    </div>

    <div class="section nursing">
      <h2>Nursing</h2>
      <p>If you are nursing, please avoid eating anything spicy (hot sauce, hot peppers, curry, etc.) that might upset baby’s tummy for 24 hours preceding your scheduled session.</p>
      <p>Please if you are breastfeeding do NOT drink caffeine or coffee before your session – I know this is hard but baby will be wired if you have caffeine.</p>
      <p>If you notice baby has a lot of gas after feedings please check with your pediatrician and bring gas drops (Tummyease or other brand) to your session. The most common reason a baby will not settle for a session is gas pressure/discomfort.</p>
    </div>

    <div class="section feeding">
      <h2>Feeding</h2>
      <p>Feed the baby as much as possible in the 24 hours preceding your session – this will help minimize the amount baby needs to feed during the session, and will help baby sleep as long and as soundly as possible. Feed baby 2-3 hours before your session and not again until you arrive. This feeding is planned in your session time and it’s not rushed.</p>
      <p class="note">Please bring an extra bottle of formula or breastmilk to the session if possible – sometimes a small amount of milk in a bottle can quickly soothe a baby back to sleep without requiring a full feeding.</p>
      <p>I will respect your wishes if you choose not to use a bottle, but please understand we may have to pass on some poses if baby will not settle in position, and I cannot use a bottle to soothe them into the pose.</p>
    </div>

    <div class="inside-photo" role="img" aria-label="Photo of a sleeping newborn resting on folded hands beside a small striped plush bunny on a white blanket"></div>
  </section>
</body>
</html>
```